The Brackenfell Raffle Competition - Coming Soon Poster

Our company is about to start operating a monthly prize competition, where entrants buy a ticket, answer the question and if they get it correct, have a chance of winning £10,000. Tickets will be mainly sold in pubs and restaurants.

This A3-sized poster will be one of the first ways people hear about The Brackenfell Raffle. Ideally it will be eye-catching, exciting and stylish. It could feature images of money, or things you can do with significant amounts of money.

Whichever design I choose, I hope to create a range of posters and flyers based on the same fundamental themes - so this design is actually the start of the brand image also, and that means more work for the same designer!

I would like the poster to feature some kind of catchy tag-line, like "Get ready to play..." / "Coming Soon..." / "Prepare yourself for...etc.,

- and also instruction on how they will play - for example - 1)Get a ticket 2)Answer the question 3)Cross fingers, or
1)Get a ticket 2)Fill it in 3)Imagine £10,000. Hold that thought.
or
Get a Ticket - Complete the Question - Good luck!

Also, possibly include this:
"Your'e much, much more likely to win £10,000 with The Brackenfell Raffle than a six-number lottery. Why? Because we don't give ridiculously huge prizes that virtually no-one wins, and we'd rather give you more than the price of a round at your local. So we settled with a nice compromise - Ten Grand."

- but overall, its up to you with the design and the wording! If you can think of different wording, give it a go!!

MUST INCLUDE
"We will give 2% of all ticket sales to charities each month."

The cost of entry is £3, the prize(s) are £10,000. The competition will operate monthly, and the first month's competition will start on 1 July 2011. We already have a logo, in lots of different file formats, see attached zip file.

Thank you

Martin

Just an update:

Just a point to note - for some reason the image files such as TIF or PNG that I sent to you have messed up colours. The colours should look like they do in the BMP and JPG files :) the colour codes (RBG) are also in a text file in the zip folder if you need them

Thank you!

Target Market(s)

Adults, in the UK, both male and female. Usually, the target market will be in a pub, bar or restaurant.

Industry/Entity Type

It Company

Requirements
Must have
• A nice sort of 'photoshop feel' - basically something that looks really artistic. Lots of posters can look cheesy or overcrowded.
Nice to have
• Something that can be used again and again in different forms to create brand identity.

Possibly include photos of english money, £20 notes for example.
Should not have
• Should not look cheesy or cheap =]

```html
<!DOCTYPE html>
<html lang="en">
<head>
<meta charset="utf-8">
<title>The Brackenfell Raffle – Coming Soon</title>
<link rel="stylesheet" href="https://fonts.googleapis.com/css2?family=Arimo:wght@700&family=Archivo+Black&display=swap">
<style>
  :root {
    --page: #ffffff;
    --poster: #000000;
    --ink: #ffffff;
    --brand-red: #c41e3a;
    --brand-orange: #f08a1c;
    --gold-light: #fff4b0;
    --gold-mid: #f2c230;
    --gold-deep: #b07a10;
    --sack-light: #d9cdb4;
    --sack-dark: #8f8470;
  }
  html, body {
    margin: 0;
    padding: 0;
    width: 1200px;
    height: 900px;
    overflow: hidden;
    background: var(--page);
  }
  .canvas {
    position: relative;
    width: 1200px;
    height: 900px;
    overflow: hidden;
    background: var(--page);
    font-family: "Arimo", Arial, sans-serif;
    font-weight: 700;
    color: var(--ink);
  }
  .poster {
    position: absolute;
    left: 238px;
    top: 0;
    width: 730px;
    height: 900px;
    overflow: hidden;
    background: var(--poster);
  }
  .brand {
    position: absolute;
    left: 8px;
    top: 18px;
    display: flex;
    align-items: center;
    gap: 34px;
  }
  .brand-mark {
    width: 160px;
    height: 160px;
    border-radius: 50%;
    background: var(--brand-orange);
  }
  .brand-name {
    margin: 0;
    font-size: 47px;
    font-weight: 700;
    color: var(--brand-red);
    white-space: nowrap;
  }
  .money-bags {
    position: absolute;
    left: 232px;
    top: 425px;
    width: 498px;
    height: 315px;
    border-radius: 60px 60px 30px 30px;
    background: radial-gradient(ellipse at 50% 45%, var(--sack-light) 0%, var(--sack-dark) 70%, rgba(0,0,0,0) 100%);
  }
  .word {
    position: absolute;
    margin: 0;
    line-height: 1;
    white-space: nowrap;
  }
  .headline { left: 125px; top: 176px; font-size: 62px; }
  .w-enter { left: 19px; top: 264px; font-size: 50px; }
  .w-for { left: 215px; top: 332px; font-size: 22px; }
  .w-your { left: 259px; top: 304px; font-size: 58px; }
  .w-chance { left: 442px; top: 377px; font-size: 40px; }
  .w-to { left: 44px; top: 434px; font-size: 44px; }
  .w-win { left: 107px; top: 418px; font-size: 66px; }
  .prize {
    position: absolute;
    left: 4px;
    top: 505px;
    width: 726px;
    height: 215px;
  }
  .prize text {
    font-family: "Archivo Black", "Arial Black", sans-serif;
  }
  .how-title {
    position: absolute;
    left: 87px;
    top: 706px;
    margin: 0;
    font-size: 13px;
  }
  .steps {
    position: absolute;
    left: 35px;
    top: 736px;
    margin: 0;
    padding: 0;
    list-style: none;
    font-size: 28px;
    line-height: 41px;
  }
  .steps .cont { display: block; padding-left: 32px; line-height: 32px; }
  .details {
    position: absolute;
    right: 14px;
    top: 860px;
    margin: 0;
    font-size: 12px;
    line-height: 17px;
    text-align: right;
  }
</style>
</head>
<body>
<div class="canvas">
  <main class="poster">
    <header class="brand">
      <span class="brand-mark" aria-hidden="true"></span>
      <h1 class="brand-name">The Brackenfell Raffle</h1>
    </header>

    <div class="money-bags" role="img" aria-label="Sacks overflowing with British banknotes"></div>

    <p class="word headline">Are You Ready?</p>
    <p class="word w-enter">Enter</p>
    <p class="word w-for">for</p>
    <p class="word w-your">your</p>
    <p class="word w-chance">chance</p>
    <p class="word w-to">to</p>
    <p class="word w-win">win...</p>

    <svg class="prize" viewBox="0 0 726 215" role="img" aria-label="£10,000">
      <defs>
        <linearGradient id="gold" x1="0" y1="0" x2="0" y2="1">
          <stop offset="0" stop-color="var(--gold-light)"/>
          <stop offset="0.45" stop-color="var(--gold-mid)"/>
          <stop offset="1" stop-color="var(--gold-deep)"/>
        </linearGradient>
      </defs>
      <text x="0" y="155" font-size="150" fill="#ffffff">£</text>
      <text x="104" y="186" font-size="225" fill="url(#gold)" stroke="#000000" stroke-width="8" paint-order="stroke" textLength="566" lengthAdjust="spacingAndGlyphs">10,000</text>
    </svg>

    <h2 class="how-title">How it Works</h2>
    <ol class="steps">
      <li>1) Get a ticket</li>
      <li>2) Answer the question on the ticket</li>
      <li>3) Imagine an extra £10,000 in your<span class="cont">pocket!</span></li>
    </ol>

    <p class="details">Just £3 a ticket · Monthly draws from 1 July 2011<br>We will give 2% of all ticket sales to charities each month.</p>
  </main>
</div>
</body>
</html>
```